AUTO SPAREPART DISTRIBUTOR BUSINESS CARD

Our company need a business card design. We are a distributor and importer of car spareparts for ZOVA and MERLOTA car model. We would like the design with White color back ground and attractive color for the fonts and looks clean, simple and attractive.
We provide the company information and the brand logo (ZOVA, MERLOTA, DUP, 738) should be put on the business card.

Thank you

Target Market(s)

Auto spareparts retailer shop and supplier.

Industry/Entity Type

Business

Contact Information for Business Card

The front side of the business card only contain company informations, and the back side may be put the brand logo (ZOVA, MERLOTA, DUP AND 738).

Requirements
Must have
• On the back side ( the brand logo) position , should have a transparency world map picture ( i uploaded the world map picture sample ).
• Also, need to put some words of " AUTO PARTS DISTRIBUTOR " (may be put on any appropriate place).

```html
<!DOCTYPE html>
<html lang="en">
<head>
<meta charset="utf-8">
<title>DUP Business Card</title>
<link rel="stylesheet" href="https://fonts.googleapis.com/css2?family=Lato:wght@100;300;400;700&display=swap">
<style>
  :root {
    --bg: #ececec;
    --card: #ffffff;
    --green: #6a9b3d;
    --green-light: #8cc04a;
    --black: #0d0d0d;
    --ink: #2b2b2b;
    --muted: #8a8a8a;
    --brand-blue: #1f3f7a;
    --brand-red: #c8102e;
    --map-tone: #b9c9d6;
  }
  * { margin: 0; padding: 0; box-sizing: border-box; }
  html, body { width: 1200px; height: 586px; overflow: hidden; }
  body {
    background: var(--bg);
    font-family: "Lato", sans-serif;
    color: var(--ink);
    position: relative;
  }
  .card {
    position: absolute;
    top: 128px;
    width: 502px;
    height: 302px;
    background: var(--card);
    overflow: hidden;
  }
  .card--front { left: 61px; }
  .card--back { left: 619px; }
  .bands { position: absolute; left: 0; top: 0; width: 502px; height: 302px; }

  /* front */
  .front-mark {
    position: absolute;
    left: 150px;
    top: 98px;
    width: 58px;
    height: 58px;
    background: var(--green);
  }
  .front-name {
    position: absolute;
    left: 222px;
    top: 84px;
    font-weight: 100;
    font-size: 110px;
    line-height: 1;
    letter-spacing: 2px;
    color: var(--black);
  }
  .tagline {
    position: absolute;
    left: 323px;
    top: 274px;
    font-weight: 300;
    font-size: 12.5px;
    line-height: 16px;
    letter-spacing: 0.3px;
    color: #fff;
  }

  /* back */
  .back-mark {
    position: absolute;
    left: 76px;
    top: 104px;
    display: flex;
    align-items: center;
    gap: 10px;
  }
  .back-mark__square { width: 34px; height: 34px; background: var(--green); }
  .back-mark__name {
    font-weight: 100;
    font-size: 50px;
    line-height: 1;
    color: var(--black);
  }
  .person {
    position: absolute;
    right: 28px;
    top: 43px;
    text-align: right;
  }
  .person__name { font-weight: 300; font-size: 18px; color: var(--green); letter-spacing: 0.5px; line-height: 22px; }
  .person__role { font-weight: 300; font-size: 12.5px; color: var(--muted); line-height: 18px; }
  .contacts {
    position: absolute;
    right: 10px;
    top: 96px;
    list-style: none;
  }
  .contacts__item {
    display: flex;
    justify-content: flex-end;
    align-items: center;
    gap: 8px;
    height: 22.4px;
    font-weight: 300;
    font-size: 12.5px;
    color: var(--ink);
  }
  .contacts__icon { width: 12px; height: 12px; flex: none; }
  .address {
    position: absolute;
    left: 15px;
    top: 261px;
    font-weight: 300;
    font-size: 12px;
    line-height: 16.5px;
    color: #fff;
  }
  .world-map {
    position: absolute;
    left: 286px;
    top: 224px;
    width: 210px;
    height: 58px;
    border-radius: 40%;
    background: radial-gradient(ellipse at center, rgba(185,201,214,0.45) 0%, rgba(185,201,214,0.2) 55%, rgba(185,201,214,0) 75%);
  }
  .partners {
    position: absolute;
    right: 26px;
    top: 238px;
    display: flex;
    gap: 14px;
    align-items: flex-end;
  }
  .partner {
    display: flex;
    flex-direction: column;
    align-items: center;
    gap: 3px;
    font-weight: 700;
    font-size: 10.5px;
    letter-spacing: 0.4px;
    line-height: 12px;
  }
  .partner__dot { width: 16px; height: 16px; border-radius: 50%; }
  .partner--merlota { color: var(--brand-blue); }
  .partner--merlota .partner__dot { background: var(--brand-blue); }
  .partner--zova { color: var(--brand-red); }
  .partner--zova .partner__dot { background: var(--brand-red); }
  .partner--738 { color: var(--brand-red); }
  .partner--738 .partner__dot { background: var(--brand-red); }
</style>
</head>
<body>

  <section class="card card--front">
    <svg class="bands" viewBox="0 0 502 302" aria-hidden="true">
      <polygon points="0,284 279,284 264,302 0,302" fill="var(--black)"/>
      <polygon points="312,256 502,256 502,302 265,302" fill="var(--green)"/>
    </svg>
    <div class="front-mark"></div>
    <div class="front-name">DUP</div>
    <div class="tagline">AUTO PARTS DISTRIBUTOR</div>
  </section>

  <section class="card card--back">
    <svg class="bands" viewBox="0 0 502 302" aria-hidden="true">
      <polygon points="293,284 502,284 502,302 314,302" fill="var(--black)"/>
      <polygon points="0,256 249,256 310,302 0,302" fill="var(--green)"/>
    </svg>

    <div class="back-mark">
      <span class="back-mark__square"></span>
      <span class="back-mark__name">DUP</span>
    </div>

    <div class="person">
      <div class="person__name">RIAN SUTANTO</div>
      <div class="person__role">Director</div>
    </div>

    <ul class="contacts">
      <li class="contacts__item">rian.sut22
        <svg class="contacts__icon" viewBox="0 0 12 12"><circle cx="6" cy="6" r="6" fill="var(--green)"/></svg>
      </li>
      <li class="contacts__item">+62-21-48320715
        <svg class="contacts__icon" viewBox="0 0 12 12"><path d="M1 4 Q6 0 11 4 L10 5.5 8 4.5 8 3.5 Q6 3 4 3.5 L4 4.5 2 5.5Z M3 6 L9 6 10.5 11 1.5 11Z" fill="var(--green)"/></svg>
      </li>
      <li class="contacts__item">+62-21-48320716
        <svg class="contacts__icon" viewBox="0 0 12 12"><rect x="3" y="1" width="6" height="3" fill="var(--green)"/><rect x="0.5" y="4.5" width="11" height="5" rx="1" fill="var(--green)"/><rect x="3" y="8" width="6" height="3.5" fill="var(--green)" stroke="#fff" stroke-width="0.8"/></svg>
      </li>
      <li class="contacts__item">+62-812-7390415
        <svg class="contacts__icon" viewBox="0 0 12 12"><rect x="3" y="0.5" width="6.5" height="11" rx="1" fill="none" stroke="var(--green)" stroke-width="1"/><rect x="4" y="2" width="4.5" height="7" fill="var(--green)" opacity="0.35"/></svg>
      </li>
      <li class="contacts__item">sales@dup-parts.example
        <svg class="contacts__icon" viewBox="0 0 12 12"><rect x="0.5" y="2" width="11" height="8" fill="var(--green)"/><path d="M0.5 2 L6 6.5 11.5 2" fill="none" stroke="#fff" stroke-width="1"/></svg>
      </li>
    </ul>

    <div class="world-map" role="img" aria-label="Faint transparent world map behind the partner brands"></div>

    <div class="partners">
      <div class="partner partner--merlota"><span class="partner__dot"></span>MERLOTA</div>
      <div class="partner partner--zova"><span class="partner__dot"></span>ZOVA</div>
      <div class="partner partner--738"><span class="partner__dot"></span>738</div>
    </div>

    <div class="address">
      Taman Sari Residence 4, Blok C-07 No. B-18 ,<br>
      Kembangan, Jakarta Barat, Indonesia (11610)
    </div>
  </section>

</body>
</html>
```